Lydfern Primary School

We need to improve on our designs for a local School, Lydfern Primary.
One file contains the correct information required on the sign.
Our Mock ups are suggestions.
The School Uniform is blue -
We had these comments from our Client.
I can't decide whether to change the blue and try green to represent our commitment to outdoors, or maybe a combination of colours from the school badge, For the main sign options , I like them both but wondered if there was a way of combining the two? Slightly bigger badge.

I've included the files for the smaller signs if you were happy to provide a service to include all. We are a sign business focusing on other projects and external support will help. Thanks - Dermot.

```html
<!DOCTYPE html>
<html lang="en">
<head>
<meta charset="utf-8">
<title>Lydfern Primary – Wayfinding Signs</title>
<link rel="stylesheet" href="https://fonts.googleapis.com/css2?family=Poppins:wght@700&display=swap">
<style>
  :root {
    --backdrop: #676767;
    --school-blue: #327abd;
    --band-blue: #2b6aa3;
    --field-green: #a0cb48;
    --sign-white: #ffffff;
  }
  html, body {
    margin: 0;
    padding: 0;
    width: 1200px;
    height: 1200px;
    overflow: hidden;
    background: var(--backdrop);
  }
  .sign-sheet {
    display: block;
    width: 1200px;
    height: 1200px;
  }
  .sign-text,
  .school-name {
    font-family: "Poppins", sans-serif;
    font-weight: 700;
    fill: var(--sign-white);
    text-anchor: middle;
  }
  .panel-blue { fill: var(--school-blue); }
  .panel-band { fill: var(--band-blue); }
  .panel-green { fill: var(--field-green); }
  .frame-line { fill: none; stroke: var(--sign-white); stroke-width: 2.5; }
  .arrow { fill: var(--sign-white); }
</style>
</head>
<body>
<svg class="sign-sheet" viewBox="0 0 1200 1200" xmlns="http://www.w3.org/2000/svg">
  <defs>
    <clipPath id="breakfast-shape">
      <path d="M387 196 L480 196 C520 196 510 98 600 98 C690 98 680 196 720 196 L814 196 Q824 196 824 206 L824 544 Q824 554 814 554 L387 554 Q377 554 377 544 L377 206 Q377 196 387 196 Z"/>
    </clipPath>
    <clipPath id="intercom-shape">
      <rect x="377" y="656" width="447" height="446" rx="10"/>
    </clipPath>
  </defs>

  <!-- Breakfast Club sign -->
  <g class="sign sign--breakfast-club">
    <g clip-path="url(#breakfast-shape)">
      <rect class="panel-blue" x="377" y="90" width="447" height="340"/>
      <rect class="panel-band" x="377" y="424" width="447" height="13"/>
      <rect class="panel-green" x="377" y="437" width="447" height="117"/>
    </g>
    <path class="frame-line" d="M390 210 L485 210 C525 210 515 111 600 111 C685 111 675 210 715 210 L811 210 L811 542 L390 542 Z"/>
    <text class="school-name" x="600" y="186" font-size="28">Lydfern</text>
    <text class="school-name" x="600" y="220" font-size="28">Primary</text>
    <text class="sign-text" x="600" y="338" font-size="67">Breakfast</text>
    <text class="sign-text" x="600" y="398" font-size="67">Club</text>
    <path class="arrow" d="M460 485 L504 454 L504 472 L742 472 L742 498 L504 498 L504 518 Z"/>
  </g>

  <!-- Intercom sign -->
  <g class="sign sign--intercom">
    <g clip-path="url(#intercom-shape)">
      <rect class="panel-blue" x="377" y="656" width="447" height="286"/>
      <rect class="panel-band" x="377" y="942" width="447" height="12"/>
      <rect class="panel-green" x="377" y="954" width="447" height="148"/>
    </g>
    <rect class="frame-line" x="390" y="669" width="421" height="420" rx="6"/>
    <text class="sign-text" x="601" y="746" font-size="60">Please use</text>
    <text class="sign-text" x="601" y="802" font-size="60">intercom</text>
    <text class="sign-text" x="601" y="858" font-size="60">to contact</text>
    <text class="sign-text" x="601" y="914" font-size="60">office</text>
    <path class="arrow" d="M444 1018 L494 983 L494 1003 L757 1003 L757 1034 L494 1034 L494 1054 Z"/>
  </g>
</svg>
</body>
</html>
```